Enduring Hurricane Rosalind: Cover Design Project

Designers! 28 October 2025 was a day I will never forget. I am writing a book about my experience.

Enduring Rosalind is a gripping, first-person account of surviving the first-ever Category 5 hurricane to directly strike Jamaica. The narrative follows a father, his girlfriend, and their 20-month-old son as they endure three weeks of total infrastructure collapse—no water, power, or cellular service.

Unlike a typical disaster memoir, this book focuses on modern preparedness and self-reliance. It details the strategic use of solar power (Voltaro units), satellite technology (Skyvane), and the psychological resilience required to protect a family while the island’s landscape is literally rewritten by 160mph winds. It is a story of survival, the "inconvenience of convenience" regarding elderly parents, and the hard lessons learned about government and infrastructure fragility.
Updates

Designers, thank you all for the amazing designs. You are making it a tough decision to pick the best one! I appreciate you all.

Gerald

Target Market(s)

Residents of hurricane-prone regions (Caribbean, Gulf Coast, etc.). "Preppers" and survivalists interested in off-grid technology. Parents interested in family protection and emergency planning. Travelers and expats living in the tropics.

Industry/Entity Type

I will be requesting a file for an e-book, paperback, hardcover, and listenly. High-resolution front cover (for eBook). Full wrap (Front, Spine, and Back) for print (Brindle BPS/FolioCrest specs). Source files (AI, PSD, or EPS). I would like a jpg mock-up for marketing purposes once finalized.

Font styles to use
Serif

Requirements
Must have
• Tone: Intense, authentic, resilient, and sophisticated. It should feel like a "Journalistic Memoir" meets a "Survival Guide." Visual Style: High contrast. I want to see a juxtaposition between the chaos of nature (darkness, storm, destroyed palms) and the glow of human resilience (light from a solar generator, a safe room, or a glowing window). Color Palette: Deep storm grays, teals, and blacks, contrasted with "survival orange" (evoking Voltaro/preparedness gear) or a warm, safe yellow light. Main Title: Enduring Rosalind (Must be bold, commanding, and easily readable in thumbnail size). Subtitle: Resilience, Solar Power, and the Category 5 hurricane that Changed Jamaica (Clean, modern sans-serif). Author Name: Dr. Gerald Whitcombe
Nice to have
• The Storm’s Power: Imagery of the catastrophic wind or the "270-degree turn" on a satellite map. Massive, uprooted tropical trees (the "toy trees" mentioned in the book). Modern Survival Tech: A subtle nod to solar panels or a portable power station. The concept of "Light in the Darkness." The Human Element: A silhouette of a family, or a small, poignant item like a child’s toy (representing the author's son, Tobin) amidst the debris. Jamaican Identity: Subtle Caribbean cues—the shape of the island, tropical flora (even if damaged), or colors that hint at the Jamaican flag without being cliché. The "Sanctuary": The idea of an interior "safe room" or closet being the last line of defense.

```html
<!DOCTYPE html>
<html lang="en">
<head>
<meta charset="UTF-8">
<title>Enduring Rosalind — Book Cover</title>
<link href="https://fonts.googleapis.com/css2?family=Oswald:wght@400;500;600;700&display=swap" rel="stylesheet">
<style>
  :root {
    --backdrop: #c6c1bc;
    --cover-deep: #0a1212;
    --cover-teal: #1c3132;
    --cover-mist: #4a605e;
    --storm-light: #9aa9a6;
    --survival-orange: #ef7a1f;
    --window-glow: #f59a36;
    --ember: #b4621e;
    --subtitle-grey: #dcdfdb;
    --author-cream: #ece5d6;
  }
  * { margin: 0; padding: 0; box-sizing: border-box; }
  html, body {
    width: 1200px;
    height: 1200px;
    overflow: hidden;
    background: var(--backdrop);
  }
  .canvas {
    position: relative;
    width: 1200px;
    height: 1200px;
    background: var(--backdrop);
  }
  .book-cover {
    position: absolute;
    left: 300px;
    top: 90px;
    width: 600px;
    height: 980px;
    overflow: hidden;
    background: var(--cover-deep);
    font-family: "Oswald", sans-serif;
  }
  .storm-sky {
    position: absolute;
    left: 0; top: 0;
    width: 100%;
    height: 520px;
    background:
      radial-gradient(ellipse 22% 7% at 68% 8%, rgba(220,228,225,0.75), transparent 75%),
      radial-gradient(ellipse 70% 14% at 55% 4%, rgba(140,158,155,0.55), transparent 70%),
      radial-gradient(circle at 45% 26%, transparent 0 90px, rgba(80,100,98,0.55) 110px, transparent 190px),
      radial-gradient(ellipse 30% 16% at 45% 26%, rgba(60,78,76,0.7), transparent 80%),
      radial-gradient(ellipse 25% 12% at 15% 10%, rgba(8,14,14,0.9), transparent 80%),
      radial-gradient(ellipse 55% 30% at 50% 48%, rgba(110,132,128,0.45), transparent 75%),
      linear-gradient(180deg, #1a2828 0%, #223433 40%, #1e3130 100%);
  }
  .ground-scene {
    position: absolute;
    left: 0; top: 520px;
    width: 100%;
    height: 460px;
    background:
      radial-gradient(ellipse 9% 7% at 80% 20%, rgba(245,154,54,0.95), rgba(245,154,54,0.35) 55%, transparent 100%),
      radial-gradient(ellipse 30% 22% at 78% 22%, rgba(240,130,40,0.28), transparent 80%),
      radial-gradient(ellipse 12% 30% at 36% 45%, rgba(6,10,10,0.95), transparent 85%),
      radial-gradient(ellipse 14% 36% at 54% 42%, rgba(6,10,10,0.95), transparent 85%),
      radial-gradient(ellipse 45% 14% at 55% 72%, rgba(180,98,30,0.55), transparent 80%),
      radial-gradient(ellipse 35% 45% at 8% 35%, rgba(8,16,16,0.85), transparent 85%),
      linear-gradient(90deg, rgba(40,62,60,0.6) 0%, transparent 40%, transparent 70%, rgba(30,40,40,0.7) 100%),
      linear-gradient(180deg, #1e3130 0%, #15221f 30%, #101917 65%, #0a1111 100%);
  }
  .title {
    position: absolute;
    top: 150px;
    left: 0;
    width: 100%;
    text-align: center;
    color: var(--survival-orange);
    font-weight: 600;
    font-size: 124px;
    line-height: 140px;
    letter-spacing: 1px;
    text-transform: uppercase;
    text-shadow: 0 4px 18px rgba(0,0,0,0.45);
  }
  .subtitle {
    position: absolute;
    top: 452px;
    left: 40px;
    width: 520px;
    text-align: center;
    color: var(--subtitle-grey);
    font-weight: 500;
    font-size: 26px;
    line-height: 1.25;
    text-shadow: 0 2px 8px rgba(0,0,0,0.6);
  }
  .author {
    position: absolute;
    top: 850px;
    left: 0;
    width: 100%;
    text-align: center;
    color: var(--author-cream);
    font-weight: 500;
    font-size: 48px;
    line-height: 1;
    letter-spacing: 3px;
    text-transform: uppercase;
  }
</style>
</head>
<body>
<main class="canvas">
  <section class="book-cover">
    <div class="storm-sky" role="img" aria-label="Dark swirling hurricane eye with pale storm light breaking through the clouds"></div>
    <div class="ground-scene" role="img" aria-label="Storm-bent palms in mist, a family of four in silhouette facing a small house with a glowing orange window and a solar panel on warm-lit ground"></div>
    <h1 class="title">Enduring<br>Rosalind</h1>
    <p class="subtitle">Resilience, Solar Power, and the Category 5 Hurricane That Changed Jamaica</p>
    <p class="author">Dr. Gerald Whitcombe</p>
  </section>
</main>
</body>
</html>
```